Dorvelan Swimming & Athletics Center

We need Business Card for a Athletics center
The logo frome the Uploaded Files ( b card fimal)
Οn one side of card we need the logo of company the Contact and the website:
1. Address:(Limassol, Cyprus 12-14 Stavrinelou str,Ano Trimeni,P.C. 4832)

2.Phone number: (+357) 25-704263

3. Mail: info@dorvelanfit.example

3. Website: www.dorvelanfit.example

Οn the other side of the card we need to write the sport of the company:

1. Artistic Gymnastics
2. Swimming
3. Gym - Fitness
4. Programs
5. Dancing
5.Tennis

From the Uploaded Files you can get the logo.In a logo is behind the black color which can be removed from logo.

Υou can use that color you want.
.
Updates

Industry/Entity Type

Business

Font styles to use
Decorative

Colors
0555a3
ffcf3e
3176b5
0692cd
add136
f04a50
000000
cfcfcf
9d9d9d

Requirements
Should not have
• photos with faces
• photo fro the Website:www.dorvelanfit.example

```html
<!DOCTYPE html>
<html lang="en">
<head>
<meta charset="utf-8">
<title>Dorvelan Swimming &amp; Athletics Center – Business Card</title>
<link rel="stylesheet" href="https://fonts.googleapis.com/css2?family=Roboto:wght@300;400;900&display=swap">
<style>
  :root {
    --backdrop: #2b2d31;
    --card-black: #050505;
    --gold-light: #ffe27a;
    --gold: #ffcf3e;
    --gold-deep: #e59a1c;
    --ink: #3a2a08;
    --line-gold: #d9a52c;
  }
  * { box-sizing: border-box; margin: 0; padding: 0; }
  html, body {
    width: 1200px; height: 1000px; overflow: hidden;
    background: var(--backdrop);
    font-family: "Roboto", Arial, sans-serif;
  }
  .canvas { position: relative; width: 1200px; height: 1000px; }

  .card {
    position: absolute;
    width: 600px; height: 340px;
    border-radius: 24px;
    overflow: hidden;
    background: var(--card-black);
    box-shadow: 0 18px 40px rgba(0,0,0,.45);
  }

  /* Front: contact side */
  .card--front { left: 70px; top: 110px; }
  .card--front .brand-row {
    position: absolute; left: 0; right: 0; top: 0; height: 180px;
    display: flex; align-items: center; justify-content: center; gap: 26px;
  }
  .brand-name {
    font-weight: 900; font-size: 62px; letter-spacing: 2px;
    color: var(--gold);
  }
  .brand-dot {
    width: 74px; height: 74px; border-radius: 50%;
    border: 3px solid var(--gold);
  }
  .gold-rule {
    position: absolute; left: 0; right: 0; top: 188px; height: 2px;
    background: var(--line-gold);
  }
  .contact-band {
    position: absolute; left: 0; right: 0; top: 196px; bottom: 0;
    background: linear-gradient(90deg, var(--gold-deep), var(--gold) 35%, var(--gold-light) 70%, var(--gold));
    padding: 30px 26px 0;
    color: var(--ink);
    font-size: 13.5px; font-weight: 400;
  }
  .contact-row {
    display: flex; justify-content: space-between; gap: 16px;
    margin-bottom: 26px;
  }
  .contact-row--single { justify-content: flex-start; }
  .contact-item { display: flex; align-items: center; gap: 8px; white-space: nowrap; }
  .contact-item svg { width: 14px; height: 14px; flex: none; }

  /* Back: sports side */
  .card--back { left: 530px; top: 550px; }
  .card--back .gold-edge {
    position: absolute; left: 0; right: 0; bottom: 0; height: 48px;
    background: linear-gradient(90deg, var(--gold-deep), var(--gold) 40%, var(--gold-light) 75%, var(--gold));
  }
  .sports-layout {
    position: absolute; left: 0; right: 0; top: 0; bottom: 48px;
    display: flex; align-items: center; justify-content: center; gap: 26px;
  }
  .mark {
    display: flex; flex-direction: column; align-items: center; gap: 8px;
  }
  .mark .brand-dot { width: 64px; height: 64px; }
  .mark-name { font-weight: 900; font-size: 15px; letter-spacing: 1px; color: var(--gold); }
  .divider { width: 2px; height: 130px; background: var(--line-gold); }
  .sports-list {
    list-style: none;
    color: var(--gold);
    font-weight: 300; font-size: 24px; line-height: 1.05;
  }
</style>
</head>
<body>
<main class="canvas">

  <section class="card card--front" aria-label="Business card, contact side">
    <div class="brand-row">
      <span class="brand-name">DORVELAN</span>
      <span class="brand-dot"></span>
    </div>
    <div class="gold-rule"></div>
    <div class="contact-band">
      <div class="contact-row">
        <span class="contact-item">
          <svg viewBox="0 0 24 24" fill="none" stroke="currentColor" stroke-width="2"><path d="M5 3h4l2 5-3 2a12 12 0 0 0 6 6l2-3 5 2v4a2 2 0 0 1-2 2A17 17 0 0 1 3 5a2 2 0 0 1 2-2z"/></svg>
          (+357) 25-704263
        </span>
        <span class="contact-item">
          <svg viewBox="0 0 24 24" fill="none" stroke="currentColor" stroke-width="2"><rect x="3" y="5" width="18" height="14"/><path d="M3 5l9 8 9-8"/></svg>
          info@dorvelanfit.example
        </span>
        <span class="contact-item">
          <svg viewBox="0 0 24 24" fill="none" stroke="currentColor" stroke-width="2"><circle cx="12" cy="12" r="9"/><path d="M3 12h18M12 3c3 3 3 15 0 18M12 3c-3 3-3 15 0 18"/></svg>
          www.dorvelanfit.example
        </span>
      </div>
      <div class="contact-row contact-row--single">
        <span class="contact-item">
          <svg viewBox="0 0 24 24" fill="none" stroke="currentColor" stroke-width="2"><path d="M12 22s7-7 7-12a7 7 0 0 0-14 0c0 5 7 12 7 12z"/><circle cx="12" cy="10" r="2.5"/></svg>
          Limassol, Cyprus 12-14 Stavrinelou str,Ano Trimeni,P.C. 4832
        </span>
      </div>
    </div>
  </section>

  <section class="card card--back" aria-label="Business card, sports side">
    <div class="sports-layout">
      <div class="mark">
        <span class="brand-dot"></span>
        <span class="mark-name">DORVELAN</span>
      </div>
      <div class="divider"></div>
      <ul class="sports-list">
        <li>Artistic Gymnastics</li>
        <li>Swiming Gym - Fitness</li>
        <li>Programs</li>
        <li>Dancing</li>
        <li>Tennis</li>
      </ul>
    </div>
    <div class="gold-edge"></div>
  </section>

</main>
</body>
</html>
```